Med Spa business card design with logo

Need a logo design and business card for our new company Velora Skinworks Med Spa. We are a medical office that deals with high end clients. We offer them skin care products which include NERVAX, lip augmentation, and various laser for the skin. I king of like the logo attached, maybe something along those lines but also open to any logo concept.
Updates

Target Market(s)

Out target audience are male and females in the age range of 21-80 years of age

Industry/Entity Type

Medical

Contact Information for Business Card

woukd like front of card to have logo and business name VELORA SKINWORKS MEDSPA. Back of card employee name and phone number along with instagram logo and user name

Font styles to use
Serif
Sans Serif

Requirements
Must have
• prefer monochromatic look white, black, gold
Should not have
• not too colorful

```html
<!DOCTYPE html>
<html lang="en">
<head>
<meta charset="utf-8">
<title>Velora Skinworks MedSpa – Business Card</title>
<link rel="stylesheet" href="https://fonts.googleapis.com/css2?family=Libre+Baskerville:wght@700&family=PT+Sans&display=swap">
<style>
  :root {
    --backdrop: #3b3b3b;
    --card: #202020;
    --ink-light: #ffffff;
    --ink-dark: #1e1e1e;
    --gold: #d4ae0c;
    --serif: "Libre Baskerville", Georgia, serif;
    --sans: "PT Sans", Arial, sans-serif;
  }
  * { margin: 0; padding: 0; box-sizing: border-box; }
  html, body { width: 1200px; height: 1200px; overflow: hidden; }
  body { background: var(--backdrop); position: relative; }

  .card {
    position: absolute;
    top: 160px;
    width: 503px;
    height: 880px;
    background: var(--card);
    box-shadow: 0 6px 18px rgba(0,0,0,0.45);
  }
  .card--front { left: 50px; }
  .card--back { left: 648px; }

  .brand-mark {
    position: absolute;
    left: 130px;
    top: 80px;
    width: 240px;
    height: 240px;
  }
  .brand-name {
    position: absolute;
    left: 0;
    right: 0;
    top: 398px;
    text-align: center;
    font-family: var(--serif);
    font-weight: 700;
    font-size: 27px;
    color: var(--ink-light);
    white-space: nowrap;
  }

  .employee-name {
    position: absolute;
    left: 127px;
    top: 168px;
    font-family: var(--serif);
    font-weight: 700;
    font-size: 48px;
    color: var(--ink-light);
    white-space: nowrap;
  }
  .employee-phone {
    position: absolute;
    left: 127px;
    top: 258px;
    font-family: var(--sans);
    font-size: 38px;
    color: var(--ink-light);
    letter-spacing: 0.5px;
  }
  .social-band {
    position: absolute;
    left: 0;
    top: 357px;
    width: 314px;
    height: 56px;
    background: var(--gold);
    display: flex;
    align-items: center;
  }
  .social-icon {
    margin-left: 40px;
    width: 44px;
    height: 44px;
  }
  .social-handle {
    margin-left: 20px;
    font-family: var(--sans);
    font-size: 34px;
    color: var(--ink-dark);
  }
</style>
</head>
<body>
  <section class="card card--front">
    <svg class="brand-mark" viewBox="0 0 240 240" aria-hidden="true">
      <circle cx="120" cy="120" r="110" fill="none" stroke="var(--ink-light)" stroke-width="14"/>
    </svg>
    <p class="brand-name">Velora Skinworks MedSpa</p>
  </section>

  <section class="card card--back">
    <h1 class="employee-name">jane DOE</h1>
    <p class="employee-phone">555 555 5555</p>
    <div class="social-band">
      <svg class="social-icon" viewBox="0 0 44 44" aria-hidden="true">
        <rect x="4" y="4" width="36" height="36" fill="none" stroke="var(--ink-dark)" stroke-width="5"/>
      </svg>
      <span class="social-handle">@janedoe</span>
    </div>
  </section>
</body>
</html>
```